HIgh-end jewelry designer needs a business card design

I need a business card design for the ecclectic & rather expensive jewelry designs. My approach to my work is to combine very old jewelry offset with contemporary items. I enjoy the idea of legacy as well as repurposing finely crafted items that are not possible to create any longer. My desire is to celebrate the past in a contemporary & funky way. The name of my business is VELLORINE. I see my business card design as simple & yet enigmatic as possible. In the end... clean, simple & understated is the look I am after. Thank you for your consideration...

Target Market(s)

I will use this business card for the trade as well as customers

Industry/Entity Type

Business

Contact Information for Business Card

Marta Quorrin Owner/Designer 555-203-7718

Requirements
Must have
• Clean & simple sophisticated design using the word "Vellorinne" as the logo. I like the idea of a play on the word itself, perhaps even using different fonts (i.e.: a bold helvetica combined with a lovely script). I'm afraid to say more because I don't want to limit creative input. Gosh, sometimes it's ok to break the rules!
Nice to have
• In my mind, I have imagined this business card to be simple, using my company name "Vellorine" in a playful yet sophisticated manner. I believe that doing something beautifully simple can be a true challenge. I have imagined something with just black & white, however I am open to ideas... after all that's why I'm here!
Should not have
• As Mozart once said... "It has too many notes!" I know I'm being silly, but I don't want it to be complicated or overly ornate.

```html
<!DOCTYPE html>
<html lang="en">
<head>
<meta charset="utf-8">
<title>Vellorine Business Card</title>
<link href="https://fonts.googleapis.com/css2?family=Arimo&family=Josefin+Sans:wght@300&display=swap" rel="stylesheet">
<style>
  :root {
    --page-bg: #f7f7f7;
    --card-black: #050708;
    --wordmark: #cfcfcf;
    --bar-grey: #2f3031;
    --contact-text: #dcdcdc;
    --shine: #3a3a3a;
  }
  html, body {
    margin: 0;
    padding: 0;
    width: 1200px;
    height: 900px;
    overflow: hidden;
    background: var(--page-bg);
  }
  .canvas {
    position: relative;
    width: 1200px;
    height: 900px;
  }
  .card {
    position: absolute;
    left: 343px;
    width: 510px;
    height: 285px;
    border-radius: 38px;
    background: var(--card-black);
    overflow: hidden;
    box-shadow: 6px 8px 14px rgba(0, 0, 0, 0.22);
  }
  .card--front { top: 137px; }
  .card--back { top: 438px; }
  .wordmark {
    position: absolute;
    left: 0;
    right: 0;
    top: 116px;
    margin: 0;
    text-align: center;
    font-family: "Josefin Sans", sans-serif;
    font-weight: 300;
    font-size: 34px;
    letter-spacing: 13px;
    padding-left: 13px;
    line-height: 1;
    color: var(--wordmark);
  }
  .shine-band {
    position: absolute;
    top: 0;
    bottom: 0;
    left: 156px;
    width: 202px;
    background: linear-gradient(90deg,
      var(--card-black) 0%,
      #0d0e0f 25%,
      var(--shine) 50%,
      #0d0e0f 75%,
      var(--card-black) 100%);
  }
  .contact-bar {
    position: absolute;
    left: 29px;
    width: 455px;
    top: 225px;
    height: 34px;
    border-radius: 7px;
    background: var(--bar-grey);
    display: flex;
    align-items: center;
    justify-content: center;
    font-family: "Arimo", sans-serif;
    font-size: 17.5px;
    color: var(--contact-text);
    white-space: nowrap;
  }
</style>
</head>
<body>
  <main class="canvas">
    <section class="card card--front">
      <h1 class="wordmark">VELLORINE</h1>
    </section>
    <section class="card card--back">
      <div class="shine-band"></div>
      <p class="contact-bar">Marta Quorrin Owner/Designer 555-203-7718</p>
    </section>
  </main>
</body>
</html>
```